Harbourline Plumbing business card full re design & logo design

Harbourline Plumbing is a Sydney based mechanical plumbing contractor company.
We would like a full redesign with new logo etc which we can take to a future website, uniforms, vehicle sign writing etc.
Blue is my preferred choice of colour but i would be open to see a couple of alternatives thrown in the mix to see how they compare. I am open to see on white cards, black cards etc. Open to many new ideas.
Please see attached original business cards which have been used for the last 5 years.

Target Market(s)

Mechanical services industry.

Industry/Entity Type

Plumbing

Contact Information for Business Card

Colin Ferraday
Director

Mob: 0427 560 918
Email: colin@harbourlineplumbing.net.au
PO BOX 716
Wendale NSW 2158
Lic: 583926d

Logo Text

Harbourline Plumbing

Font styles to use
Sans Serif

Colors
0655a3
3276b5
0792cd
33a6d7
85cae6
000000
333333
474747

Requirements
Must have
• Things that make it very professional and very well presented.
Nice to have
• Same description or very similar to attached uploaded file
Should not have
• Anything that makes it look unprofessional or cartoony.

```html
<!DOCTYPE html>
<html lang="en">
<head>
<meta charset="utf-8">
<title>Harbourline Plumbing – Business Card</title>
<link href="https://fonts.googleapis.com/css2?family=Open+Sans:wght@400;600&family=Marcellus+SC&display=swap" rel="stylesheet">
<style>
  :root {
    --brand-blue: #0655a3;
    --ink: #333333;
    --ink-soft: #474747;
    --rule: #c8c8c8;
    --paper: #ffffff;
    --stage: #000000;
  }
  * { box-sizing: border-box; margin: 0; padding: 0; }
  html, body { width: 1200px; height: 900px; overflow: hidden; background: var(--stage); }
  body { position: relative; font-family: "Open Sans", sans-serif; }

  .card { position: absolute; width: 477px; height: 294px; }
  .card-front {
    left: 116px; top: 275px; background: var(--paper);
    border-radius: 0 46px 0 46px; color: var(--ink);
  }
  .card-back {
    left: 622px; top: 276px; background: var(--brand-blue);
    border-radius: 46px 0 46px 0; color: var(--paper); text-align: center;
  }

  .licence { position: absolute; left: 28px; top: 28px; font-size: 14px; color: var(--ink); }
  .licence b { color: var(--brand-blue); font-weight: 600; }

  .brand-block { position: absolute; right: 26px; top: 40px; text-align: right; }
  .brand-name {
    font-size: 25px; font-weight: 600; color: var(--brand-blue);
    letter-spacing: 1px; line-height: 1.25; text-transform: uppercase;
  }
  .brand-name span { display: block; }
  .brand-tagline { margin-top: 10px; font-size: 10.5px; letter-spacing: 1.6px; color: var(--brand-blue); }

  .person { position: absolute; left: 26px; top: 164px; }
  .person-name { font-family: "Marcellus SC", serif; font-size: 19px; color: var(--ink); letter-spacing: .5px; }
  .person-name .first { color: var(--brand-blue); }
  .person-role { font-size: 13px; color: var(--ink-soft); margin-top: 0; }
  .rule { position: absolute; left: 82px; right: 26px; top: 193px; height: 1px; background: var(--rule); }

  .contacts { position: absolute; left: 26px; top: 209px; list-style: none; font-size: 13.5px; line-height: 17.5px; color: var(--ink); }
  .contacts li { display: flex; align-items: center; gap: 5px; }
  .contacts svg { width: 12px; height: 12px; fill: var(--brand-blue); flex: none; }

  .postal { position: absolute; right: 26px; top: 209px; text-align: right; font-size: 14px; line-height: 17.5px; color: var(--ink); }

  .back-name {
    margin-top: 70px; font-size: 36px; font-weight: 600; letter-spacing: 2px;
    text-transform: uppercase; line-height: 1.1;
  }
  .back-heading {
    margin-top: 44px; display: flex; align-items: center; justify-content: center; gap: 10px;
    font-size: 16px; font-weight: 600; letter-spacing: .2px;
  }
  .back-heading::before, .back-heading::after { content: ""; width: 44px; height: 1px; background: rgba(255,255,255,.8); }
  .services { list-style: none; display: flex; flex-wrap: wrap; justify-content: center; gap: 8px 10px; margin: 10px auto 0; width: 380px; font-size: 14px; }
  .services li { display: flex; align-items: center; gap: 4px; }
  .services svg { width: 7px; height: 10px; fill: var(--paper); }
</style>
</head>
<body>

<section class="card card-front" aria-label="Business card front">
  <p class="licence"><b>LIC:</b> 583926D</p>

  <div class="brand-block">
    <p class="brand-name"><span>Harbourline</span><span>Plumbing</span></p>
    <p class="brand-tagline">MECHANICAL PLUMBING SERVICES</p>
  </div>

  <div class="person">
    <p class="person-name"><span class="first">Colin</span> Ferraday</p>
    <p class="person-role">Director</p>
  </div>
  <div class="rule"></div>

  <ul class="contacts">
    <li><svg viewBox="0 0 12 12" aria-hidden="true"><path d="M1 4c0-1.5 2-2.5 5-2.5S11 2.5 11 4v1H8.5V4h-5v1H1zM2.5 6h7l1 4.5h-9z"/></svg>0427 560 918</li>
    <li><svg viewBox="0 0 12 12" aria-hidden="true"><path d="M1 2.5h10v7H1zM1.6 3.2 6 6.6l4.4-3.4"/><path d="M1.6 3.2 6 6.6l4.4-3.4" fill="none" stroke="#fff" stroke-width="1"/></svg>colin@harbourlineplumbing.net.au</li>
    <li><svg viewBox="0 0 12 12" aria-hidden="true"><circle cx="6" cy="6" r="5.5"/><path d="M6 .5v11M.5 6h11" stroke="#fff" stroke-width=".8"/></svg>www.harbourlineplumbing.net.au</li>
  </ul>

  <address class="postal" style="font-style:normal">PO Box 716<br>Wendale<br>NSW 2158</address>
</section>

<section class="card card-back" aria-label="Business card back">
  <p class="back-name">Harbourline<br>Plumbing</p>
  <p class="back-heading">MECHANICAL PLUMBING SERVICES</p>
  <ul class="services">
    <li><svg viewBox="0 0 7 10" aria-hidden="true"><path d="M3.5 0C3 2 0 4.5 0 6.5a3.5 3.5 0 0 0 7 0C7 4.5 4 2 3.5 0z"/></svg>Make Good</li>
    <li><svg viewBox="0 0 7 10" aria-hidden="true"><path d="M3.5 0C3 2 0 4.5 0 6.5a3.5 3.5 0 0 0 7 0C7 4.5 4 2 3.5 0z"/></svg>Refurbishment</li>
    <li><svg viewBox="0 0 7 10" aria-hidden="true"><path d="M3.5 0C3 2 0 4.5 0 6.5a3.5 3.5 0 0 0 7 0C7 4.5 4 2 3.5 0z"/></svg>Tenancy Fit Out</li>
    <li><svg viewBox="0 0 7 10" aria-hidden="true"><path d="M3.5 0C3 2 0 4.5 0 6.5a3.5 3.5 0 0 0 7 0C7 4.5 4 2 3.5 0z"/></svg>Plant Room Works</li>
    <li><svg viewBox="0 0 7 10" aria-hidden="true"><path d="M3.5 0C3 2 0 4.5 0 6.5a3.5 3.5 0 0 0 7 0C7 4.5 4 2 3.5 0z"/></svg>Shut Downs</li>
    <li><svg viewBox="0 0 7 10" aria-hidden="true"><path d="M3.5 0C3 2 0 4.5 0 6.5a3.5 3.5 0 0 0 7 0C7 4.5 4 2 3.5 0z"/></svg>Change Overs</li>
  </ul>
</section>

</body>
</html>
```